Design a double sided business card

We are looking for a clean, eye-catching, and contemporary design that enhances the brand and presents a premium, professional image. Our preference is for a brown card with black gloss detailing and embossed elements; however, we are open to creative input and design suggestions that best achieve a strong visual impact.

Please see the attached existing business card for reference. We use both black and brown colours consistently across our branding.

On sample provided

```html
<!DOCTYPE html>
<html lang="en">
<head>
<meta charset="utf-8">
<title>Valmore – Business Card</title>
<link rel="stylesheet" href="https://fonts.googleapis.com/css2?family=Montserrat:wght@400;700;800&display=swap">
<style>
  :root {
    --backdrop: #a4a4a4;
    --card: #c8b59b;
    --ink: #0c0c0c;
  }
  * { margin: 0; padding: 0; box-sizing: border-box; }
  html, body {
    width: 1200px; height: 1200px; overflow: hidden;
    background: var(--backdrop);
    font-family: "Montserrat", Arial, sans-serif;
    color: var(--ink);
  }
  .canvas { position: relative; width: 1200px; height: 1200px; }
  .card {
    position: absolute; left: 145px; width: 909px; height: 518px;
    background: var(--card);
  }
  .card--front { top: 62px; }
  .card--back { top: 622px; }

  .brand-wordmark {
    position: absolute; left: 0; right: 0; top: 58px;
    text-align: center;
    font-weight: 800; font-size: 104px; letter-spacing: 0.09em;
    line-height: 1;
  }
  .divider {
    position: absolute; left: 161px; width: 585px; top: 212px;
    height: 2px; background: var(--ink);
  }
  .identity {
    position: absolute; left: 0; right: 0; top: 240px;
    display: flex; justify-content: center; align-items: center; gap: 14px;
  }
  .identity__name { font-weight: 700; font-size: 32px; letter-spacing: 0.02em; }
  .identity__bar { width: 2px; height: 38px; background: var(--ink); }
  .identity__role { font-weight: 400; font-size: 24px; padding-top: 4px; }

  .contacts {
    position: absolute; top: 354px;
    list-style: none; font-size: 24px; line-height: 36.5px;
  }
  .contacts--left { left: 86px; }
  .contacts--right { left: 450px; }
  .contacts li { display: flex; align-items: flex-start; gap: 12px; }
  .contacts .icon { width: 20px; height: 36px; flex: none; }
  .contacts .icon svg { width: 18px; height: 18px; margin-top: 9px; fill: var(--ink); }

  .back-mark {
    position: absolute; inset: 0;
    display: flex; justify-content: center; align-items: center; gap: 26px;
  }
  .back-mark__square { width: 64px; height: 64px; background: var(--ink); }
  .back-mark__name { font-weight: 800; font-size: 96px; letter-spacing: 0.09em; line-height: 1; }
</style>
</head>
<body>
<main class="canvas">
  <section class="card card--front">
    <div class="brand-wordmark">VALMORE</div>
    <div class="divider"></div>
    <div class="identity">
      <span class="identity__name">RAVI DHAL</span>
      <span class="identity__bar"></span>
      <span class="identity__role">Director</span>
    </div>

    <ul class="contacts contacts--left">
      <li><span class="icon"><svg viewBox="0 0 24 24"><path d="M6.6 10.8a15 15 0 0 0 6.6 6.6l2.2-2.2a1 1 0 0 1 1-.25 11.4 11.4 0 0 0 3.6.57 1 1 0 0 1 1 1V20a1 1 0 0 1-1 1A17 17 0 0 1 3 4a1 1 0 0 1 1-1h3.5a1 1 0 0 1 1 1c0 1.25.2 2.45.57 3.57a1 1 0 0 1-.25 1z"/></svg></span>0800 246 7315</li>
      <li><span class="icon"><svg viewBox="0 0 24 24"><path d="M6 2h12v5H6zM4 8h16a2 2 0 0 1 2 2v7h-4v5H6v-5H2v-7a2 2 0 0 1 2-2zm4 8v4h8v-4z"/></svg></span>07700900461</li>
      <li><span class="icon"><svg viewBox="0 0 24 24"><path d="M2 5h20v2l-10 6L2 7zm0 4.3 10 6 10-6V19H2z"/></svg></span>ravi@valmore.co.uk</li>
    </ul>

    <ul class="contacts contacts--right">
      <li><span class="icon"><svg viewBox="0 0 24 24"><path d="M12 2a10 10 0 1 0 0 20 10 10 0 0 0 0-20zm0 2c.9 0 2.2 1.7 2.8 5H9.2C9.8 5.7 11.1 4 12 4zM4.3 11h4.6a20 20 0 0 0 0 2H4.3a8 8 0 0 1 0-2zm6.6 0h2.2a18 18 0 0 1 0 2h-2.2a18 18 0 0 1 0-2zm4.2 0h4.6a8 8 0 0 1 0 2h-4.6a20 20 0 0 0 0-2zM12 20c-.9 0-2.2-1.7-2.8-5h5.6c-.6 3.3-1.9 5-2.8 5z"/></svg></span>www.valmore.co.uk</li>
      <li><span class="icon"><svg viewBox="0 0 24 24"><path d="M12 2a7 7 0 0 0-7 7c0 5 7 13 7 13s7-8 7-13a7 7 0 0 0-7-7zm0 9.5A2.5 2.5 0 1 1 12 6.5a2.5 2.5 0 0 1 0 5z"/></svg></span><span>The Green Millers Lane<br>Ashworthy AB4 2CD</span></li>
    </ul>
  </section>

  <section class="card card--back">
    <div class="back-mark">
      <span class="back-mark__square"></span>
      <span class="back-mark__name">VALMORE</span>
    </div>
  </section>
</main>
</body>
</html>
```